Business Card Design Project

Hi. We need a new business card for Brightfield Partners, a consultancy that helps people with online marketing strategy and solutions.

We have a new logo and now need the info presented - front and back of business card.

FRONT

Logo

Online strategy, consulting and coaching
Varlo Admarket consulting
Search Engine Optimisation
Internet Lead Generation
Domain name broking

BACK

Tom Bradwell-Jones
+ 61 83215 9076
+ 61 (0) 418 536 207
tom@brightfieldpartners.com.au
www.brightfieldpartners.com.au

Talkora: tombradwelljones
PO Box 312, South Perth, Western Australia 6951

Target Market(s)

Business owners, corporates

Industry/Entity Type

Marketing

Requirements
Must have
• double sided
size: 86 x 54mm
supplied as one pdf with crop marks shown (+- 1mm, with 2-3 mm bleed)

```html
<!DOCTYPE html>
<html lang="en">
<head>
<meta charset="utf-8">
<title>Brightfield Partners – Business Card Concepts</title>
<link rel="stylesheet" href="https://fonts.googleapis.com/css2?family=Arimo:wght@400;700&display=swap">
<style>
  :root {
    --board: #c9b797;
    --label: #2b2218;
    --card-white: #ffffff;
    --card-black: #231f20;
    --card-blue-dark: #1d4784;
    --card-blue-light: #2d64ae;
    --brand-blue: #1f4f8f;
    --brand-orange: #f7941d;
    --text-dark: #333333;
    --text-blue: #2a5aa0;
    --text-white: #ffffff;
  }
  * { margin: 0; padding: 0; box-sizing: border-box; }
  html, body {
    width: 1200px; height: 788px; overflow: hidden;
    background: var(--board);
    font-family: "Arimo", Arial, sans-serif;
  }
  .board { position: relative; width: 1200px; height: 788px; }

  .side-label {
    position: absolute; font-size: 21px; color: var(--label);
    transform: translateX(-50%); white-space: nowrap;
  }

  .card {
    position: absolute; width: 508px; height: 319px; border-radius: 22px;
    overflow: hidden; box-shadow: 0 2px 6px rgba(0,0,0,.25);
  }
  .card--white { background: var(--card-white); }
  .card--black { background: var(--card-black); }
  .card--blue { background: linear-gradient(90deg, var(--card-blue-dark), var(--card-blue-light)); }

  .brand { position: absolute; display: flex; flex-direction: column; }
  .brand__row { display: flex; align-items: center; gap: 12px; }
  .brand__dot { border-radius: 50%; background: var(--brand-orange); flex: none; }
  .brand__name { font-weight: 700; color: var(--brand-blue); white-space: nowrap; letter-spacing: -0.5px; }
  .brand__url { font-weight: 700; color: var(--brand-blue); letter-spacing: 2.4px; }
  .card--black .brand__name, .card--black .brand__url,
  .card--blue .brand__name, .card--blue .brand__url { color: var(--text-white); }

  .brand--small { left: 26px; top: 40px; }
  .brand--small .brand__dot { width: 40px; height: 40px; }
  .brand--small .brand__name { font-size: 30px; }
  .brand--small .brand__url { font-size: 10.5px; margin: 14px 0 0 28px; }

  .brand--large { left: 50%; top: 48px; transform: translateX(-50%); align-items: center; }
  .brand--large .brand__dot { width: 52px; height: 52px; }
  .brand--large .brand__name { font-size: 38px; }
  .brand--large .brand__url { font-size: 12px; margin-top: 22px; letter-spacing: 2.8px; }

  .name-bar {
    position: absolute; left: 300px; top: 150px; width: 208px; height: 35px;
    display: flex;
  }
  .name-bar__label {
    flex: 1; background: linear-gradient(90deg, #1c3f78, #2e63ad);
    color: var(--text-white); font-size: 13.5px; padding: 10px 0 0 13px; white-space: nowrap;
  }
  .name-bar__accent { width: 28px; background: var(--brand-orange); }

  .contacts { position: absolute; left: 305px; top: 207px; list-style: none; }
  .contacts li {
    display: flex; align-items: center; gap: 5px;
    font-size: 12.5px; color: var(--text-dark); height: 19.7px; white-space: nowrap;
  }
  .contacts svg { width: 11px; height: 11px; flex: none; }

  .address {
    position: absolute; left: 25px; top: 267px;
    font-size: 12.5px; line-height: 20px; color: var(--text-dark);
  }

  .services-list { position: absolute; left: 138px; top: 211px; list-style: none; }
  .services-list li {
    display: flex; align-items: center; gap: 7px;
    font-size: 12.5px; color: var(--text-blue); height: 19.6px; white-space: nowrap;
  }
  .services-list .bullet-dot {
    width: 11px; height: 11px; border-radius: 50%; border: 2px solid var(--brand-orange); flex: none;
  }

  .services-grid {
    position: absolute; left: 0; top: 227px; width: 100%;
    color: var(--text-white); font-size: 13px;
  }
  .services-grid__lead { text-align: center; margin-bottom: 9px; }
  .services-grid__cols { display: grid; grid-template-columns: 205px 190px; margin-left: 68px; row-gap: 9px; }
  .services-grid span::before { content: "▪ "; font-size: 10px; vertical-align: 1px; }
</style>
</head>
<body>
<main class="board">

  <span class="side-label" style="left:318px; top:17px;">back</span>
  <span class="side-label" style="left:895px; top:17px;">front - 1</span>
  <span class="side-label" style="left:326px; top:405px;">front - 2</span>
  <span class="side-label" style="left:895px; top:405px;">front - 3</span>

  <!-- Back -->
  <section class="card card--white" style="left:70px; top:48px;">
    <div class="brand brand--small">
      <div class="brand__row"><span class="brand__dot"></span><span class="brand__name">Brightfield Partners</span></div>
      <span class="brand__url">brightfieldpartners.com.au</span>
    </div>
    <div class="name-bar">
      <div class="name-bar__label">Tom Bradwell-Jones</div>
      <div class="name-bar__accent"></div>
    </div>
    <ul class="contacts">
      <li><svg viewBox="0 0 12 12"><path d="M3 1 L5 3.5 L4 5 Q5 7 7 8 L8.5 7 L11 9 L9.5 11 Q3 10 1 2.5 Z" fill="#555"/></svg>+ 61 83215 9076</li>
      <li><svg viewBox="0 0 12 12"><rect x="3" y="1" width="6" height="10" rx="1" fill="#555"/><rect x="4" y="2.3" width="4" height="5" fill="#fff"/></svg>+ 61 (0) 418 536 207</li>
      <li><svg viewBox="0 0 12 12"><rect x="1" y="3" width="10" height="7" fill="none" stroke="#555" stroke-width="1.2"/><path d="M1 3 L6 7 L11 3" fill="none" stroke="#555" stroke-width="1.2"/></svg>tom@brightfieldpartners.com.au</li>
      <li><svg viewBox="0 0 12 12"><circle cx="6" cy="6" r="5" fill="#3aa0dc"/></svg>tombradwelljones</li>
      <li><svg viewBox="0 0 12 12"><circle cx="6" cy="6" r="4.5" fill="#1f4f8f"/></svg>www.brightfieldpartners.com.au</li>
    </ul>
    <p class="address">PO Box 312, South Perth<br>Western Australia 6951</p>
  </section>

  <!-- Front 1 -->
  <section class="card card--white" style="left:640px; top:48px;">
    <div class="brand brand--large">
      <div class="brand__row"><span class="brand__dot"></span><span class="brand__name">Brightfield Partners</span></div>
      <span class="brand__url">brightfieldpartners.com.au</span>
    </div>
    <ul class="services-list">
      <li><span class="bullet-dot"></span>Online strategy, consulting and coaching</li>
      <li><span class="bullet-dot"></span>Varlo Admarket consulting</li>
      <li><span class="bullet-dot"></span>Search Engine Optimisation</li>
      <li><span class="bullet-dot"></span>Internet Lead Generation</li>
      <li><span class="bullet-dot"></span>Domain name broking</li>
    </ul>
  </section>

  <!-- Front 2 -->
  <section class="card card--black" style="left:70px; top:436px;">
    <div class="brand brand--large">
      <div class="brand__row"><span class="brand__dot"></span><span class="brand__name">Brightfield Partners</span></div>
      <span class="brand__url">brightfieldpartners.com.au</span>
    </div>
    <div class="services-grid">
      <p class="services-grid__lead"><span>Online strategy, consulting and coaching</span></p>
      <div class="services-grid__cols">
        <span>Varlo Admarket consulting</span><span>Search Engine Optimisation</span>
        <span>Internet Lead Generation</span><span>Domain name broking</span>
      </div>
    </div>
  </section>

  <!-- Front 3 -->
  <section class="card card--blue" style="left:640px; top:436px;">
    <div class="brand brand--large">
      <div class="brand__row"><span class="brand__dot"></span><span class="brand__name">Brightfield Partners</span></div>
      <span class="brand__url">brightfieldpartners.com.au</span>
    </div>
    <div class="services-grid">
      <p class="services-grid__lead"><span>Online strategy, consulting and coaching</span></p>
      <div class="services-grid__cols">
        <span>Varlo Admarket consulting</span><span>Search Engine Optimisation</span>
        <span>Internet Lead Generation</span><span>Domain name broking</span>
      </div>
    </div>
  </section>

</main>
</body>
</html>
```